QRN Law Letterhead

Want law firm letterhead - both in terms of a pdf file that I can use electronically as letterhead by adding it as a background - and in terms of a file that I can send to a company to create actual letterhead.
Industry/Entity Type
Law Firm
Font styles to use
Sans Serif
Requirements
Must have
- Should have the following information (you can decide where to place):
- My name - Emil Vostrakian
- My email - emil@qrnlegalgroup.example
- My address - 2861 Corvella Parkway 318-742
- San Jose, California 95342
- Website - www.qrnlegalgroup.example
- Phone - 408-297-1586
- Fax - 408-853-2941
- The logo I attached
Nice to have
- I think I would prefer to have a black and white color scheme.
- I don't necessarily need a title after my name, but I have seen a few design submissions that include a generic title. The title I would use is "IP Litigator & Trademark Attorney"

```html
<!DOCTYPE html>
<html lang="en">
<head>
<meta charset="utf-8">
<title>QRN Law Letterhead</title>
<link rel="stylesheet" href="https://fonts.googleapis.com/css2?family=Lato:wght@400;700&display=swap">
<style>
  :root {
    --backdrop: #e4e4e4;
    --paper: #ffffff;
    --brand: #5a7483;
    --ink: #3a3a3a;
    --rule: #9a9a9a;
  }
  * { margin: 0; padding: 0; box-sizing: border-box; }
  html, body {
    width: 1200px;
    height: 1200px;
    overflow: hidden;
    background: var(--backdrop);
    font-family: "Lato", sans-serif;
  }
  .letterhead {
    position: absolute;
    left: 208px;
    top: 40px;
    width: 784px;
    height: 1120px;
    background: var(--paper);
  }
  .brand {
    position: absolute;
    left: 64px;
    top: 82px;
    height: 56px;
    display: flex;
    align-items: center;
    gap: 10px;
  }
  .brand-mark {
    width: 52px;
    height: 52px;
    border: 5px solid var(--brand);
    border-radius: 50%;
  }
  .brand-name {
    font-family: "Lato", sans-serif;
    font-weight: 400;
    font-size: 40px;
    letter-spacing: 1px;
    color: var(--brand);
    line-height: 1;
  }
  .contact {
    position: absolute;
    left: 515px;
    top: 44px;
    border-left: 1px solid var(--rule);
    padding: 2px 0 2px 19px;
    font-size: 12.5px;
    font-style: normal;
    color: var(--ink);
    line-height: 17.5px;
  }
  .contact-name {
    font-weight: 700;
    font-size: 13px;
    color: var(--brand);
    margin-bottom: 4px;
  }
  .contact-address { margin-bottom: 8px; }
  .contact-line {
    display: flex;
    align-items: center;
    gap: 6px;
  }
  .contact-line svg {
    width: 10px;
    height: 10px;
    flex: none;
    fill: var(--brand);
  }
</style>
</head>
<body>
  <main class="letterhead">
    <div class="brand">
      <div class="brand-mark"></div>
      <span class="brand-name">QRN Law</span>
    </div>

    <address class="contact">
      <div class="contact-name">Emil Vostrakian</div>
      <div class="contact-address">
        2861 Corvella Parkway 318-742<br>
        San Jose, California 95342
      </div>
      <div class="contact-line">
        <svg viewBox="0 0 10 10" aria-hidden="true"><path d="M2 0.5 L3.6 2.6 L2.7 3.6 Q4 6 6.4 7.3 L7.4 6.4 L9.5 8 L8.3 9.5 Q3.5 9 0.5 1.7 Z"/></svg>
        <span>408-297-1586</span>
      </div>
      <div class="contact-line">
        <svg viewBox="0 0 10 10" aria-hidden="true"><path d="M2.5 0.5 H7.5 V3.5 H9.5 V7.5 H7.5 V9.5 H2.5 V7.5 H0.5 V3.5 H2.5 Z M3.5 1.5 V3.5 H6.5 V1.5 Z M3.5 6 V8.5 H6.5 V6 Z"/></svg>
        <span>408-853-2941</span>
      </div>
      <div class="contact-line">
        <svg viewBox="0 0 10 10" aria-hidden="true"><path d="M0.5 2 H9.5 V8 H0.5 Z M1.2 2.6 L5 5.6 L8.8 2.6 V3.3 L5 6.3 L1.2 3.3 Z" fill-rule="evenodd"/></svg>
        <span>emil@qrnlegalgroup.example</span>
      </div>
      <div class="contact-line">
        <svg viewBox="0 0 10 10" aria-hidden="true"><path d="M5 0.5 A4.5 4.5 0 1 0 5.01 0.5 Z M5 1.3 A3.7 3.7 0 1 1 4.99 1.3 Z M4.6 1 H5.4 V9 H4.6 Z M1 4.6 H9 V5.4 H1 Z M5 1 Q2.6 5 5 9 Q2 5 5 1 Z M5 1 Q7.4 5 5 9 Q8 5 5 1 Z" fill-rule="evenodd"/></svg>
        <span>www.qrnlegalgroup.example</span>
      </div>
    </address>
  </main>
</body>
</html>
```